Create an awesome website for a medical clinic

This is a new website for a doctor's office. The site should be clean and modern, easy to navigate.

This is a wellness clinic, we want to help our clients have a healthy, active lifestyle. It should be friendly and inviting, and easy for them to call or schedule an appointment.

The site should be responsive and designed using the attached Bootstrap 3 PSD.

We will provide stock photos, until then please use stock photos from:

photoharvestbin.net or
lumapicturevault.net (preferred)

Some example sites of clean and modern designs that we like:

https://tarnelspine.example/
http://walkpastjoints.example/
http://feelingbrisker.example/

Also attached is a temporary logo you can use.
Updates

Reason: Thank you everyone for your great designs - we need a little more time so I'm extending the project.

Need extra days to review

Also, the colors in the new logo I just linked to are the final colors of the logo, so feel free to use any complimentary colors to it.

Hi everyone, The boss wants to change the layout of the site a little bit - here's the revised layout: https://www.filecrate.example/s/q8vn31kd2pxe74rt/memo%2011_29_2017.pdf?dl=0 And the graphic assets you can use are here: https://www.filecrate.example/s/q8vn31kd2pxe74rt/memo%2011_29_2017.pdf?dl=0 Feel free to change the background color of the "topbar", and change the icons of the "why people trust us" if you want, these are just temporary placeholders. Thanks for your patience and hard work!

Target Market(s)

People seeking medical treatment (wellness clinic)

Industry/Entity Type

Doctor

Number of Pages Required

1 page

Font styles to use
Sans Serif

Colors
0592cd
33a6d7
abd037
9bcb3c

Requirements
Must have
• The home page should have: a strong hero image/slideshow, clinic phone number should be prominent and at the top of the page (in the nav), a "what to expect" section (this is like a FAQs section - see attachment), and a strong call to action (a button to call or schedule an appointment).
• The what to expect section is useful so that prospective clients can determine if we're a good fit for them or not. It's a basic, first-step pre-qualification block of information.
• Social media icons which links to our social media profiles should be included.
Nice to have
• - Link to 3 most recent blog entries
• - Testimonials
• - How a multilevel nav menu looks.

```html
<!DOCTYPE html>
<html lang="en">
<head>
<meta charset="utf-8">
<title>Fernwell Medical Clinic</title>
<link href="https://fonts.googleapis.com/css2?family=Montserrat:wght@400;500;600;700&display=swap" rel="stylesheet">
<style>
:root{
  --blue:#0592cd;
  --blue-light:#33a6d7;
  --green:#9bcb3c;
  --ink:#222;
  --topbar:#f4f4f4;
  --white:#fff;
}
*{margin:0;padding:0;box-sizing:border-box}
html,body{width:1200px;height:1200px;overflow:hidden;background:var(--white)}
body{font-family:"Montserrat",sans-serif;color:var(--ink);position:relative}
.topbar{height:45px;background:var(--topbar);position:relative}
.topbar .follow{position:absolute;left:73px;top:16px;font-size:11px;letter-spacing:1.3px;text-transform:uppercase;font-weight:500}
.social{position:absolute;left:295px;top:11px;display:flex;gap:8px}
.social span{width:23px;height:23px;border-radius:50%;background:#7cc4e6;display:block}
.appointment{position:absolute;left:882px;top:0;width:244px;height:45px;background:var(--blue);color:var(--white);font-size:11px;font-weight:600;letter-spacing:1.4px;text-transform:uppercase;display:flex;align-items:center;justify-content:center}
.header{height:99px;position:relative}
.brand{position:absolute;left:73px;top:22px;display:flex;align-items:center;gap:8px}
.brand .mark{width:16px;height:16px;background:var(--green)}
.brand .name{font-size:18px;font-weight:700;color:var(--blue);letter-spacing:.3px;line-height:1.15;width:150px}
.contact{position:absolute;top:28px;display:flex;gap:17px;align-items:center}
.contact .icon{width:42px;height:42px;background:var(--blue);display:flex;align-items:center;justify-content:center}
.contact .text{font-size:9px;letter-spacing:1.2px;text-transform:uppercase;line-height:15px}
.contact .text strong{font-size:11px;font-weight:600}
.contact.phone{left:722px}
.contact.address{left:930px;top:28px}
.nav{height:60px;background:var(--blue);display:flex;justify-content:center;align-items:center;gap:57px}
.nav a{color:var(--white);text-decoration:none;font-size:13px;font-weight:500;letter-spacing:1.6px;text-transform:uppercase}
.hero{position:relative;height:606px;background:linear-gradient(180deg,#7f9a4e 0%,#a9a76a 35%,#c9aa7d 60%,#b08c70 100%)}
.hero .photo{position:absolute;inset:0;background:radial-gradient(ellipse at 60% 60%,rgba(214,160,120,.55),rgba(0,0,0,0) 60%)}
.caption{position:absolute;left:73px;top:184px;width:359px;height:236px;background:rgba(90,170,205,.72);text-align:center;color:var(--white)}
.caption h1{font-weight:500;font-size:26px;letter-spacing:2.8px;line-height:30px;margin:42px 30px 0}
.dots{position:absolute;left:18px;bottom:17px;display:flex;gap:8px}
.dots span{width:9px;height:9px;border-radius:50%;border:1.5px solid var(--white)}
.dots span.on{background:var(--white)}
.services{height:298px;background:var(--blue);position:relative}
.service{position:absolute;top:64px;width:250px;color:var(--white)}
.service h2{font-size:17px;font-weight:600;letter-spacing:2px;margin-bottom:14px}
.service p{font-size:11.4px;line-height:20.3px;margin-left:1px}
.service .more{display:inline-flex;align-items:center;justify-content:center;margin-top:22px;margin-left:2px;width:120px;height:34px;border:2px solid var(--white);border-radius:18px;font-size:10.5px;letter-spacing:1.4px;font-weight:500;text-transform:uppercase}
.intro{position:relative;height:92px}
.intro h2{position:absolute;left:72px;top:50px;font-size:23px;font-weight:500;letter-spacing:3px;line-height:28px;text-transform:uppercase}
.intro .photo{position:absolute;left:685px;top:0;width:515px;height:92px;background:linear-gradient(90deg,#d9dde0,#eef0f1 45%,#cfc6bd)}
</style>
</head>
<body>
<div class="topbar">
  <div class="follow">Follow us on social media!</div>
  <div class="social" aria-label="Social media links"><span></span><span></span><span></span></div>
  <div class="appointment">Make an appointment</div>
</div>
<header class="header">
  <div class="brand"><span class="mark"></span><span class="name">FERNWELL MEDICAL CLINIC</span></div>
  <div class="contact phone">
    <div class="icon"><svg width="22" height="26" viewBox="0 0 24 24"><path fill="#fff" d="M6.6 10.8a15.1 15.1 0 0 0 6.6 6.6l2.2-2.2c.3-.3.7-.4 1-.2 1.1.4 2.3.6 3.6.6.6 0 1 .4 1 1V20c0 .6-.4 1-1 1A17 17 0 0 1 3 4c0-.6.4-1 1-1h3.5c.6 0 1 .4 1 1 0 1.3.2 2.5.6 3.6.1.3 0 .7-.2 1z"/></svg></div>
    <div class="text"><strong>(555) 014-7730</strong><br>Fax: (555) 014-7731</div>
  </div>
  <div class="contact address">
    <div class="icon"><svg width="22" height="28" viewBox="0 0 24 30"><path fill="#fff" d="M12 1a10 10 0 0 0-10 10c0 7.5 10 18 10 18s10-10.5 10-18A10 10 0 0 0 12 1zm0 14a4 4 0 1 1 0-8 4 4 0 0 1 0 8z"/></svg></div>
    <div class="text"><strong>Suite 204, Level 2</strong><br>88 Marrowind Lane<br>Eastbrook, ST 00000</div>
  </div>
</header>
<nav class="nav">
  <a href="#">Home</a><a href="#">About us</a><a href="#">For parents</a><a href="#">For professionals</a><a href="#">For teens</a><a href="#">Blog</a><a href="#">Contact us</a>
</nav>
<section class="hero">
  <div class="photo" role="img" aria-label="Smiling couple outdoors in warm sunlight"></div>
  <div class="caption">
    <h1>We specialise in many areas, find the right clinic for you &amp; your family.</h1>
    <div class="dots"><span class="on"></span><span></span><span></span></div>
  </div>
</section>
<section class="services">
  <div class="service" style="left:75px"><h2>Selective Placement</h2><p>Lorem ipsum dolor sit amet, consec tetur adipiscing elit. Fusce ornare, turpis vel molestie euismod, lacus ipsum auctor nunc, sed finibus nibh tellus at augue.</p><span class="more">Read more</span></div>
  <div class="service" style="left:348px"><h2>Selective Placement</h2><p>Lorem ipsum dolor sit amet, consec tetur adipiscing elit. Fusce ornare, turpis vel molestie euismod, lacus ipsum auctor nunc, sed finibus nibh tellus at augue.</p><span class="more">Read more</span></div>
  <div class="service" style="left:622px"><h2>Selective Placement</h2><p>Lorem ipsum dolor sit amet, consec tetur adipiscing elit. Fusce ornare, turpis vel molestie euismod, lacus ipsum auctor nunc, sed finibus nibh tellus at augue.</p><span class="more">Read more</span></div>
  <div class="service" style="left:895px"><h2>Selective Placement</h2><p>Lorem ipsum dolor sit amet, consec tetur adipiscing elit. Fusce ornare, turpis vel molestie euismod, lacus ipsum auctor nunc, sed finibus nibh tellus at augue.</p><span class="more">Read more</span></div>
</section>
<section class="intro">
  <h2>What is the right<br>clinic for you?</h2>
  <div class="photo" role="img" aria-label="Doctor with staff in a bright clinic"></div>
</section>
</body>
</html>
```